Regional Consulting Business Needs a Business Card Design

We need a business card design for our new business based in Regional Victoria, Australia called Brindle Power. We are a consulting company with our main goal being to save people momey money and reducing their carbon footprint. Anything from water saving showerheads, to energy saving lightglobes and even to solar power. We would like to see designs that use bright colours. The final design should shout 'we are here to help you'.

Industry/Entity Type

Business

```html
<!DOCTYPE html>
<html lang="en">
<head>
<meta charset="utf-8">
<title>Brindle Power – Business Card</title>
<link rel="stylesheet" href="https://fonts.googleapis.com/css2?family=Questrial&display=swap">
<style>
  :root {
    --page-bg: #ffffff;
    --card-light: #ffffff;
    --panel-dark: #141510;
    --panel-olive: #4d4622;
    --panel-ember: #1c0e06;
    --glow-yellow: #f2e100;
    --glow-gold: #d8b800;
    --text-light: #ffffff;
    --brand-grey: #3b3b3b;
    --brand-accent: #f0a020;
  }
  * { box-sizing: border-box; margin: 0; padding: 0; }
  html, body {
    width: 1200px;
    height: 900px;
    overflow: hidden;
    background: var(--page-bg);
    font-family: "Questrial", "Century Gothic", sans-serif;
  }
  .business-card {
    position: absolute;
    left: 59px;
    top: 101px;
    width: 1063px;
    height: 650px;
    background: var(--card-light);
    box-shadow: 3px 4px 8px rgba(0, 0, 0, 0.28);
    overflow: hidden;
  }
  .contact-panel {
    position: absolute;
    left: 0;
    top: 0;
    width: 1063px;
    height: 468px;
    background:
      radial-gradient(ellipse 60% 80% at 100% 100%, var(--panel-ember) 0%, transparent 70%),
      radial-gradient(ellipse 70% 90% at 20% 0%, var(--panel-olive) 0%, transparent 75%),
      linear-gradient(100deg, #3e3a1c 0%, #25241a 45%, var(--panel-dark) 100%);
  }
  .light-streaks {
    position: absolute;
    left: 0;
    top: 0;
    width: 560px;
    height: 468px;
    background:
      radial-gradient(ellipse 12% 55% at 36% 30%, rgba(255, 255, 230, 0.75) 0%, transparent 70%),
      radial-gradient(ellipse 28% 70% at 28% 35%, rgba(242, 225, 0, 0.85) 0%, transparent 70%),
      radial-gradient(ellipse 30% 45% at 70% 85%, rgba(216, 184, 0, 0.7) 0%, transparent 70%),
      radial-gradient(ellipse 40% 30% at 15% 95%, rgba(242, 225, 0, 0.45) 0%, transparent 70%);
  }
  .person {
    position: absolute;
    right: 60px;
    top: 90px;
    text-align: right;
    color: var(--text-light);
  }
  .person-name {
    font-size: 28px;
    font-weight: 700;
    line-height: 34px;
  }
  .person-title {
    margin-top: 4px;
    font-size: 18px;
    line-height: 22px;
  }
  .divider {
    position: absolute;
    left: 532px;
    top: 198px;
    width: 531px;
    height: 3px;
    background: var(--text-light);
  }
  .contact-details {
    position: absolute;
    right: 69px;
    top: 241px;
    list-style: none;
    text-align: right;
    color: var(--text-light);
    font-size: 22px;
    line-height: 33px;
  }
  .brand {
    position: absolute;
    left: 549px;
    top: 500px;
    display: flex;
    align-items: center;
    gap: 22px;
  }
  .brand-square {
    width: 54px;
    height: 54px;
    background: var(--brand-accent);
  }
  .brand-name {
    font-size: 44px;
    color: var(--brand-grey);
    letter-spacing: 1px;
  }
</style>
</head>
<body>
  <article class="business-card">
    <section class="contact-panel">
      <div class="light-streaks" role="img" aria-label="Abstract glowing yellow light streaks sweeping across a dark background"></div>
      <div class="person">
        <p class="person-name">&lt;Insert Name&gt;</p>
        <p class="person-title">&lt;Insert Job Title&gt;</p>
      </div>
      <div class="divider"></div>
      <ul class="contact-details">
        <li>&lt;Insert Address&gt;</li>
        <li>&lt;Insert Phone &amp; Fax Numbers&gt;</li>
        <li>&lt;Insert Email Address&gt;</li>
        <li>&lt;Insert Website Address&gt;</li>
      </ul>
    </section>
    <div class="brand">
      <span class="brand-square"></span>
      <span class="brand-name">Brindle Power</span>
    </div>
  </article>
</body>
</html>
```